Simple AD for Digital Publication

Total Size 5" x 5", may include boarder or not
Image Provided; crop or use as background
Incorporate Logo and text as provided

Target Market(s)

Sound Contractors / Integrators

Industry/Entity Type

Audio Video Lighting

Requirements
Must have
• Bold Look that reflects our brand. see website: tovermundic.com - cohesive text and style

```html
<!DOCTYPE html>
<html lang="en">
<head>
<meta charset="utf-8">
<title>Tovermundic Co — Become a Dealer Ad</title>
<link rel="stylesheet" href="https://fonts.googleapis.com/css2?family=Montserrat:wght@400;500;700;800;900&family=Roboto:ital,wght@1,700;1,900&display=swap">
<style>
  :root {
    --page-bg: #e6e6e9;
    --brand-red: #b3141c;
    --brand-red-dark: #8e0f15;
    --brand-red-bright: #d9222a;
    --ink: #333335;
    --black: #050505;
    --white: #ffffff;
    --photo-top: #3d5a45;
    --photo-bottom: #968b99;
  }
  * { margin: 0; padding: 0; box-sizing: border-box; }
  html, body {
    width: 1200px;
    height: 1117px;
    overflow: hidden;
    background: var(--page-bg);
  }
  .ad {
    position: absolute;
    left: 80px;
    top: 38px;
    width: 1040px;
    height: 1040px;
    overflow: hidden;
    background: var(--black);
    font-family: "Montserrat", sans-serif;
    box-shadow: 0 6px 24px rgba(0,0,0,0.18);
  }
  .ad-backdrop {
    position: absolute;
    left: 0; top: 0;
    width: 1040px; height: 1040px;
  }
  .brand-header {
    position: absolute;
    left: 0; top: 0;
    width: 1040px; height: 199px;
    background: var(--white);
  }
  .brand-mark {
    position: absolute;
    left: 110px; top: 46px;
    width: 96px; height: 96px;
    background: var(--brand-red);
  }
  .brand-name {
    position: absolute;
    left: 238px; top: 44px;
    font-weight: 800;
    font-size: 66px;
    line-height: 1;
    letter-spacing: -1px;
    color: var(--ink);
    white-space: nowrap;
  }
  .brand-tagline {
    position: absolute;
    left: 240px; top: 122px;
    font-family: "Roboto", sans-serif;
    font-style: italic;
    font-weight: 700;
    font-size: 37px;
    line-height: 1;
    color: var(--ink);
    white-space: nowrap;
  }
  .brand-tagline .accent { color: var(--brand-red); }
  .headline {
    position: absolute;
    left: 0; top: 242px;
    width: 1040px;
    text-align: center;
    color: var(--white);
  }
  .headline-lead {
    font-weight: 400;
    font-size: 41px;
    line-height: 46px;
    letter-spacing: 0.5px;
  }
  .headline-main {
    font-weight: 900;
    font-size: 59px;
    line-height: 58px;
    letter-spacing: 0.5px;
  }
  .product-photo {
    position: absolute;
    left: 64px; top: 437px;
    width: 914px; height: 490px;
    background: linear-gradient(180deg, var(--photo-top) 0%, var(--photo-bottom) 100%);
  }
  .cta-button {
    position: absolute;
    left: 318px; top: 888px;
    width: 404px; height: 80px;
    border-radius: 40px;
    background: var(--white);
    padding: 4px;
  }
  .cta-button span {
    display: block;
    width: 100%; height: 100%;
    border-radius: 36px;
    background: linear-gradient(180deg, var(--brand-red-bright) 0%, var(--brand-red) 55%, var(--brand-red-dark) 100%);
    color: var(--white);
    font-weight: 900;
    font-size: 52px;
    line-height: 72px;
    text-align: center;
    letter-spacing: 0.5px;
  }
  .cta-caption {
    position: absolute;
    left: 0; top: 976px;
    width: 1040px;
    text-align: center;
    color: var(--white);
    font-weight: 400;
    font-size: 30px;
    line-height: 36px;
  }
  .cta-caption strong { font-weight: 700; }
</style>
</head>
<body>
  <div class="ad">
    <svg class="ad-backdrop" viewBox="0 0 1040 1040" aria-hidden="true">
      <defs>
        <linearGradient id="bandRed" x1="0" y1="0" x2="1" y2="0">
          <stop offset="0" stop-color="#9e1118"/>
          <stop offset="0.55" stop-color="#b3141c"/>
          <stop offset="0.9" stop-color="#d3222a"/>
          <stop offset="1" stop-color="#a8121a"/>
        </linearGradient>
      </defs>
      <rect x="0" y="199" width="1040" height="400" fill="url(#bandRed)"/>
      <polygon points="300,199 520,199 200,540 0,540 0,470" fill="#ffffff" opacity="0.04"/>
      <polygon points="760,199 1040,199 1040,420 900,540 700,540" fill="#000000" opacity="0.05"/>
      <polygon points="0,528 64,560 64,1040 0,1040" fill="#050505"/>
      <polygon points="1040,528 976,560 976,1040 1040,1040" fill="#050505"/>
      <polygon points="0,492 64,520 64,546 0,516" fill="#ffffff"/>
      <polygon points="1040,492 976,520 976,546 1040,516" fill="#ffffff"/>
      <rect x="0" y="900" width="1040" height="140" fill="#050505"/>
    </svg>

    <header class="brand-header">
      <div class="brand-mark"></div>
      <div class="brand-name">TOVERMUNDIC CO</div>
      <div class="brand-tagline">Stage Pocket Systems <span class="accent">Connectivity</span></div>
    </header>

    <div class="headline">
      <p class="headline-lead">PROTECT AND CONCEAL</p>
      <p class="headline-main">HIGH AND LOW VOLTAGE<br>CONNECTIVITY</p>
    </div>

    <div class="product-photo" role="img" aria-label="Photo of a black stage floor pocket set into a wooden stage floor with cables running out, evergreen garland with warm string lights behind it"></div>

    <div class="cta-button"><span>CLICK HERE</span></div>
    <p class="cta-caption">Become a <strong>Dealer</strong></p>
  </div>
</body>
</html>
```